Exciting new vermouth brand needs a brilliant label!

We need a label design for an exciting new premium Italian Vermouth brand called Lunavera Vermouth.

Lunavera Vermouth is based on a recipe that has been handed down for four generations and is made in the traditional way in the Piedmonte region of Northern Italy.

Lunavera, which means 'heavenly' in Italian has been designed to elevate classic cocktails such as the Negroni, Americano and Manhattan with a base of Italian wine blended with botanicals such as wormwood, orange peel, rhubarb and cinchona. It has a delicately balanced bittersweet profile with hints of vanilla and citrus.

Its competitors include brands such as Vecchia Ricetta, Brunetti and Fabrizzi (see the uploaded brief for more examples).

The label is for a 50cl dark bottle (please refer to the uploaded brief) and should be based on maximum dimensions of 70mm (width) x 110mm (height). There is no limit to embellishments such as foil printing, embossing or any other premium finishes. The label does not necessarily need to be rectangular.

Feedback will be given quickly and constructively after submissions to ensure that the process is as fair and useful as possible for everyone.

Target Market(s)

25-45 year old Europeans, 50:50 female:male

Industry/Entity Type

Wine / Spirits / Vermouth

Requirements
Must have
• Fantastic design that is distinct from competitors, a premium feel and great lettering.
Should not have
• Generic images or patterns that do not relate to the brand (Lunavera) or the product

```html
<!DOCTYPE html>
<html lang="it">
<head>
<meta charset="utf-8">
<title>Lunavera Vermouth – Sweet Rosso Label</title>
<link rel="stylesheet" href="https://fonts.googleapis.com/css2?family=Josefin+Sans:wght@700&family=Marcellus&family=Encode+Sans+Condensed:wght@500&display=swap">
<style>
  :root {
    --backdrop: #000000;
    --gold: #b8955e;
    --gold-light: #f3eeb8;
    --gold-mid: #d9c387;
    --cream: #ffffff;
    --ink: #0c0c0c;
    --rosso: #d8284a;
    --rosso-deep: #b20d35;
    --azzurro: #0e55c8;
    --azzurro-deep: #0a47ae;
    --white: #ffffff;
  }
  html, body {
    margin: 0;
    padding: 0;
    width: 1200px;
    height: 2560px;
    overflow: hidden;
    background: var(--backdrop);
  }
  .canvas {
    position: relative;
    width: 1200px;
    height: 2560px;
  }
  .label {
    position: absolute;
    left: 60px;
    top: 512px;
    width: 1080px;
    height: 1536px;
    overflow: visible;
  }
  .tagline {
    font-family: "Marcellus", serif;
    font-size: 27px;
    fill: var(--ink);
    text-anchor: middle;
  }
  .category {
    font-family: "Encode Sans Condensed", sans-serif;
    font-weight: 500;
    font-size: 36px;
    fill: var(--white);
    text-anchor: middle;
    letter-spacing: 1px;
  }
  .brand-name {
    font-family: "Josefin Sans", sans-serif;
    font-weight: 700;
    font-size: 104px;
    fill: var(--ink);
    text-anchor: middle;
    letter-spacing: 2px;
  }
  .variety {
    font-family: "Josefin Sans", sans-serif;
    font-weight: 700;
    font-size: 52px;
    fill: var(--white);
    text-anchor: middle;
    letter-spacing: 1px;
  }
  .serving {
    font-family: "Encode Sans Condensed", sans-serif;
    font-weight: 500;
    font-size: 48px;
    fill: var(--white);
    text-anchor: middle;
  }
  .volume {
    font-family: "Encode Sans Condensed", sans-serif;
    font-weight: 500;
    font-size: 42px;
    fill: var(--white);
    text-anchor: middle;
  }
  .rule { stroke: var(--white); stroke-width: 1.5; opacity: 0.8; }
</style>
</head>
<body>
<main class="canvas">
  <svg class="label" viewBox="0 0 720 1024" xmlns="http://www.w3.org/2000/svg" aria-label="Lunavera Vermouth Sweet Rosso label">
    <defs>
      <linearGradient id="gold-corner" x1="0" y1="0" x2="1" y2="0">
        <stop offset="0" stop-color="#d9c387"/>
        <stop offset="0.5" stop-color="#f3eeb8"/>
        <stop offset="1" stop-color="#d9c387"/>
      </linearGradient>
      <linearGradient id="rosso-band" x1="0" y1="0" x2="0" y2="1">
        <stop offset="0" stop-color="#b20d35"/>
        <stop offset="0.5" stop-color="#d8284a"/>
        <stop offset="1" stop-color="#b20d35"/>
      </linearGradient>
      <linearGradient id="azzurro-field" x1="0" y1="0" x2="0" y2="1">
        <stop offset="0" stop-color="#0a47ae"/>
        <stop offset="1" stop-color="#0e55c8"/>
      </linearGradient>
      <path id="ribbon-arc" d="M244,432 Q360,386 476,432"/>
    </defs>

    <!-- outer frame -->
    <polygon class="frame" points="360,0 720,208 720,818 360,1022 0,818 0,208" fill="var(--gold)"/>

    <!-- gold ornamental shoulders -->
    <polygon class="ornament-field" role="img" aria-label="Gold baroque scrollwork ornament"
      points="360,20 702,218 702,602 18,602 18,218" fill="url(#gold-corner)"/>

    <!-- white crest triangle -->
    <polygon class="crest" points="360,42 702,602 18,602" fill="var(--cream)"/>

    <!-- divider band -->
    <rect class="divider" x="18" y="600" width="684" height="12" fill="var(--gold)"/>

    <!-- lower blue field -->
    <polygon class="lower-field" role="img" aria-label="Blue damask pattern field"
      points="18,612 702,612 702,810 360,1002 18,810" fill="url(#azzurro-field)"/>

    <!-- red variety chevron -->
    <polygon class="variety-band" points="18,612 702,612 360,808" fill="url(#rosso-band)"/>

    <!-- crest flourish -->
    <rect class="flourish" role="img" aria-label="Gold calligraphic flourish"
      x="270" y="168" width="180" height="100" rx="50" fill="var(--gold)" opacity="0.22"/>

    <text class="tagline" x="360" y="312">ANTICA RICETTA</text>
    <text class="tagline" x="360" y="338">DI VERMOUTH PREGIATO</text>

    <!-- ribbon banner -->
    <g class="ribbon" fill="var(--gold)">
      <polygon points="212,424 252,416 262,456 196,472 214,450"/>
      <polygon points="508,424 468,416 458,456 524,472 506,450"/>
      <path d="M238,398 Q360,350 482,398 L476,448 Q360,400 244,448 Z"/>
    </g>
    <text class="category"><textPath href="#ribbon-arc" startOffset="50%">VERMOUTH</textPath></text>

    <text class="brand-name" x="360" y="572">LUNAVERA</text>

    <text class="variety" x="360" y="688">SWEET ROSSO</text>

    <text class="serving" x="360" y="867">SERVED CHILLED</text>
    <line class="rule" x1="296" y1="892" x2="424" y2="892"/>
    <text class="volume" x="360" y="929">750 ml</text>
    <line class="rule" x1="296" y1="940" x2="424" y2="940"/>
  </svg>
</main>
</body>
</html>
```